Flyer for Institute Party

This event has changed to the following - March 24th, 2017 from 4-6pm in the Halvern Medical Education Center Atrium (You can get to the Atrium from the Brenwick elevators by getting off on the 5th floor or from the Larkfield Pavilion elevators by getting off on the 5th floor). I have attached the logo of the Institute as well to add to the flyer. Also, the Morvane Institute just became and Institute in January 2017, so it would be nice to note that as part of the celebration in the flyer someplace. We have a lot to celebrate! I am looking for a fun flyer to for an Institute party. We would like to celebrate becoming an Institute and the labs within the Institute at the party.

```html
<!DOCTYPE html>
<html lang="en">
<head>
<meta charset="utf-8">
<title>Celebrate! The International Day of Awesomeness</title>
<link rel="stylesheet" href="https://fonts.googleapis.com/css2?family=Yellowtail&family=Bebas+Neue&family=Oswald:wght@400;500&family=Old+Standard+TT:wght@400;700&family=Courier+Prime&display=swap">
<style>
  :root {
    --backdrop: #e4e4e4;
    --navy: #1f3563;
    --red: #b0303a;
    --paper: #f1e6d2;
    --paper-edge: #e9dcc4;
    --ink: #3a3530;
    --rule: #fbf7ef;
  }
  * { box-sizing: border-box; margin: 0; padding: 0; }
  html, body { width: 1200px; height: 837px; overflow: hidden; background: var(--backdrop); }
  .flyer {
    position: absolute; left: 70px; top: 67px; width: 1063px; height: 686px;
    background: var(--navy); padding: 17px;
  }
  .sheet {
    position: relative; width: 100%; height: 100%;
    background: radial-gradient(ellipse at center, var(--paper) 55%, var(--paper-edge) 100%);
    outline: 2px solid var(--rule); outline-offset: -7px;
  }
  .star { position: absolute; left: 496px; top: 36px; width: 46px; height: 46px; }
  .headline {
    position: absolute; left: 340px; width: 380px; top: 66px; text-align: center; white-space: nowrap;
    font-family: "Yellowtail", "Brush Script MT", cursive; font-weight: 400; color: var(--red);
    font-size: 92px; line-height: 1.1;
  }
  .dots { position: absolute; border-top: 3px dotted var(--red); }
  .dots--celebrate-l { left: 168px; width: 163px; top: 132px; }
  .dots--celebrate-r { left: 701px; width: 155px; top: 132px; }
  .dots--by-l { left: 299px; width: 165px; top: 360px; }
  .dots--by-r { left: 536px; width: 168px; top: 360px; }
  .title-box {
    position: absolute; left: 176px; top: 181px; width: 677px; height: 123px;
    border: 4px solid var(--red); padding: 10px;
  }
  .title-box__inner {
    width: 100%; height: 100%; border: 3px dotted var(--red);
    display: flex; align-items: center; justify-content: center; white-space: nowrap; overflow: hidden;
    font-family: "Bebas Neue", "Oswald", sans-serif; font-weight: 400; color: var(--red);
    font-size: 44px; letter-spacing: 1px; text-transform: uppercase; padding-top: 4px;
  }
  .pointer { position: absolute; top: 237px; width: 82px; height: 28px; background: var(--red); border-radius: 4px 16px 16px 4px; opacity: .85; }
  .pointer--left { left: 71px; }
  .pointer--right { left: 885px; border-radius: 16px 4px 4px 16px; }
  .by-badge {
    position: absolute; left: 475px; top: 334px; width: 52px; height: 52px; border-radius: 50%;
    background: var(--red); color: var(--paper); font-family: "Yellowtail", "Brush Script MT", cursive;
    font-size: 32px; line-height: 1; display: flex; align-items: center; justify-content: center;
  }
  .tagline {
    position: absolute; left: 0; right: 0; top: 401px; text-align: center; white-space: nowrap;
    font-family: "Oswald", sans-serif; font-weight: 500; color: var(--navy);
    font-size: 20px; line-height: 24px; letter-spacing: 1px; text-transform: uppercase;
  }
  .divider-h { position: absolute; left: 14px; right: 14px; top: 437px; border-top: 2px solid var(--navy); }
  .divider-v { position: absolute; top: 452px; height: 180px; border-left: 1.5px solid var(--navy); }
  .divider-v--one { left: 362px; }
  .divider-v--two { left: 636px; }

  .presenter { position: absolute; left: 20px; top: 454px; width: 330px; }
  .presenter__label { font-family: "Courier Prime", monospace; font-size: 14px; color: var(--ink); }
  .presenter__name {
    margin-top: 56px; display: flex; align-items: center; gap: 12px; white-space: nowrap;
    font-family: "Oswald", sans-serif; font-weight: 500; font-size: 30px; color: var(--navy); text-transform: uppercase;
  }
  .presenter__dot { width: 44px; height: 44px; border-radius: 50%; background: var(--navy); flex: none; }

  .fact {
    position: absolute; left: 416px; top: 458px; width: 164px; height: 164px; border-radius: 50%;
    border: 3px dotted var(--navy); text-align: center;
  }
  .fact__head, .fact__foot {
    position: absolute; left: 0; right: 0; font-family: "Oswald", sans-serif; font-weight: 500;
    font-size: 19px; line-height: 24px; letter-spacing: 1px; text-transform: uppercase;
  }
  .fact__head { top: 16px; color: var(--red); }
  .fact__foot { bottom: 12px; color: var(--navy); }
  .fact__rule { position: absolute; left: 6px; right: 6px; border-top: 2px solid var(--navy); }
  .fact__rule--top { top: 46px; }
  .fact__rule--bottom { bottom: 42px; }
  .fact__body {
    position: absolute; left: 20px; right: 20px; top: 55px;
    font-family: "Old Standard TT", serif; color: var(--red); font-size: 11.5px; line-height: 1.3; text-transform: uppercase;
  }

  .when { position: absolute; left: 657px; top: 458px; }
  .when__date {
    font-family: "Oswald", sans-serif; font-weight: 500; font-size: 20px; line-height: 26px; white-space: nowrap;
    color: var(--red); text-transform: uppercase;
  }
  .when__time {
    margin-top: 2px; font-family: "Old Standard TT", serif; color: var(--navy); font-size: 64px; line-height: 1;
    display: flex; align-items: baseline; gap: 6px;
  }
  .when__to { font-family: "Oswald", sans-serif; font-size: 15px; line-height: 1; color: var(--red); text-transform: uppercase; align-self: center; border-bottom: 2px solid var(--red); }
  .when__pm { font-family: "Oswald", sans-serif; font-size: 20px; text-transform: uppercase; }
  .where {
    position: absolute; left: 822px; top: 460px; padding-left: 8px; border-left: 2px solid var(--navy);
    display: flex; gap: 5px;
  }
  .where__in { font-family: "Old Standard TT", serif; font-weight: 700; font-size: 13px; line-height: 20px; color: var(--red); text-transform: uppercase; }
  .where__place {
    font-family: "Oswald", sans-serif; font-weight: 500; font-size: 17.5px; line-height: 26px; white-space: nowrap;
    color: var(--red); text-transform: uppercase;
  }
  .directions {
    position: absolute; left: 657px; top: 553px; width: 340px;
    font-family: "Courier Prime", monospace; font-size: 12.5px; line-height: 1.25; color: var(--ink);
  }
</style>
</head>
<body>
<main class="flyer">
  <div class="sheet">
    <svg class="star" viewBox="0 0 48 48" aria-hidden="true">
      <polygon points="24,2 29,16 44,14 34,25 42,38 28,33 24,46 20,33 6,38 14,25 4,14 19,16" fill="#1f3563"/>
    </svg>

    <span class="dots dots--celebrate-l"></span>
    <h1 class="headline">Celebrate!</h1>
    <span class="dots dots--celebrate-r"></span>

    <div class="pointer pointer--left" role="img" aria-label="Hand-drawn pointing hand illustration"></div>
    <div class="title-box"><div class="title-box__inner">The International Day of Awesomeness</div></div>
    <div class="pointer pointer--right" role="img" aria-label="Hand-drawn pointing hand illustration"></div>

    <span class="dots dots--by-l"></span>
    <div class="by-badge">By</div>
    <span class="dots dots--by-r"></span>

    <p class="tagline">Celebrating awesomeness in the labs of the Morvane Institute</p>
    <span class="divider-h"></span>

    <section class="presenter">
      <p class="presenter__label">Proudly Brought to you by:</p>
      <p class="presenter__name"><span class="presenter__dot"></span>Morvane Institute</p>
    </section>

    <span class="divider-v divider-v--one"></span>

    <section class="fact">
      <p class="fact__head">Awesome</p>
      <span class="fact__rule fact__rule--top"></span>
      <p class="fact__body">We became an institute in January 2017!</p>
      <span class="fact__rule fact__rule--bottom"></span>
      <p class="fact__foot">Fact</p>
    </section>

    <span class="divider-v divider-v--two"></span>

    <section class="when">
      <p class="when__date">March 24th from</p>
      <p class="when__time">4<span class="when__to">to</span>6<span class="when__pm">pm</span></p>
    </section>
    <section class="where">
      <span class="where__in">In</span>
      <p class="where__place">The Halvern<br>Medical Education<br>Center Atrium</p>
    </section>
    <p class="directions">You can get to the Atrium from the Brenwick elevators by getting off on the 5th floor or from the Larkfield Pavilion elevators by getting off on the 5th floor.</p>
  </div>
</main>
</body>
</html>
```